Gains Beyond the Lantern Gate - book cover design

I need a cover designed for a new book (paperback and eBook).
The title is: “Gains Beyond the Lantern Gate” with the subtitle: “The only book you need to start investing profitably in Chinese stocks”. It is from the first time author :“Teemu Harkala“.
The following text should also be visible in the front cover: “From the founder of OrientWagerly.com” or "Founder of OrientWagerly.com".
The publisher’s logo, should also be visible somewhere on the cover (front, back or spine). The logo, along with source files are here: http://filevault.example/k7Tq2Lp
The book/paperback cover dimensions are: 5.06 x 7.81 inches (12.9 x 19.8 centimeters). Here are the book-cover templates recommended by Bookdale for a book of this size:
http://filevault.example/z3Wm9Xa (.indd)
http://filevault.example/r8Nd4Fu (.pdf)
Below is a description of the book. I don't have a specific idea or vision in mind for the cover. I'd like to see what designs and ideas ArtHuddle designers come up with.
Color red is usually associated with China, but I don’t want the book to be red. Instead the background color could be one of the publisher’s brand colors (#88C198, #017487). However I’ll leave you the designers freedom to propose any colors and combinations.
This is not an entry level book, but a very advanced level investment strategy book for international investors. It explains with concrete examples how non-Chinese citizens can best benefit from China’s economic miracle by picking the best Chinese growth stocks from New York, Hong Kong and Singapore stock exchanges.
The book cover should not have dollar signs promising easy and fast money (because easy and fast money doesn’t exist). What the book promises is a very advanced level China investing strategy, which will considerably improve international investors’ odds for big profits in the longer term.
The big investment themes in the book are China’s consumer sector and service industries.
The book cover should have some kind of reference/association to Investing and China.
The design needs to work and be effective at both a large book cover size and a small thumbnail-sized image - the way that many people browse book covers on Bookdale and other websites. Therefore, a design that relies on really small details probably won't translate at the smaller image sizes that book covers are displayed online.
Target Market(s)
International investors (~50% from western countries, 30% from Singapore/Hong Kong, Malaysia)
Industry/Entity Type
Investment
Font styles to use
Other font styles liked:
- EB Garamond, Grimson text or some other beautiful book font
Look and feel
Each slider illustrates characteristics of the customer's brand and the style your logo design should communicate.

```html
<!DOCTYPE html>
<html lang="en">
<head>
<meta charset="utf-8">
<title>Gains Beyond the Lantern Gate — Book Cover</title>
<link rel="stylesheet" href="https://fonts.googleapis.com/css2?family=Cinzel:wght@400;500&display=swap">
<style>
  :root {
    --page-bg: #ffffff;
    --cover-top: #01808f;
    --cover-bottom: #013a44;
    --title-white: #ffffff;
    --title-gold: #c9a64a;
    --accent-green: #88c198;
    --grid-line: rgba(255, 255, 255, 0.12);
    --art-glow: rgba(136, 193, 152, 0.35);
    --art-warm: rgba(201, 166, 74, 0.30);
  }
  * { box-sizing: border-box; margin: 0; padding: 0; }
  html, body {
    width: 1200px;
    height: 1200px;
    overflow: hidden;
    background: var(--page-bg);
  }
  .canvas {
    width: 1200px;
    height: 1200px;
    display: flex;
    align-items: center;
    justify-content: center;
  }
  .book-cover {
    position: relative;
    width: 700px;
    height: 1080px;
    background: linear-gradient(180deg, var(--cover-top) 0%, var(--cover-bottom) 100%);
    font-family: "Cinzel", "Trajan Pro", serif;
    color: var(--title-white);
    text-align: center;
    overflow: hidden;
  }
  .title {
    position: absolute;
    top: 80px;
    left: 0;
    right: 0;
    font-weight: 400;
    line-height: 1;
  }
  .title-line {
    display: block;
    font-size: 80px;
    letter-spacing: 1px;
    margin-bottom: 12px;
  }
  .title-accent {
    display: block;
    font-size: 138px;
    font-weight: 500;
    color: var(--title-gold);
    letter-spacing: 4px;
    margin-top: 2px;
  }
  .subtitle {
    position: absolute;
    top: 462px;
    left: 60px;
    right: 60px;
    font-size: 22px;
    line-height: 1.3;
    letter-spacing: 1px;
    text-transform: uppercase;
  }
  .founder-line {
    position: absolute;
    top: 540px;
    left: 0;
    right: 0;
    font-size: 18px;
    letter-spacing: 2px;
    color: var(--accent-green);
  }
  .cover-art {
    position: absolute;
    top: 590px;
    left: 0;
    right: 0;
    height: 330px;
    background:
      radial-gradient(ellipse 28% 34% at 30% 40%, var(--art-warm), transparent 72%),
      radial-gradient(ellipse 60% 55% at 55% 55%, var(--art-glow), transparent 78%);
  }
  .market-chart {
    position: absolute;
    top: 620px;
    left: 60px;
    width: 580px;
    height: 280px;
  }
  .market-chart .grid { stroke: var(--grid-line); stroke-width: 1; }
  .market-chart .trend {
    fill: none;
    stroke: var(--title-gold);
    stroke-width: 5;
    stroke-linejoin: round;
    stroke-linecap: round;
  }
  .market-chart .trend-area { fill: rgba(136, 193, 152, 0.18); }
  .author {
    position: absolute;
    bottom: 84px;
    left: 0;
    right: 0;
    font-size: 40px;
    letter-spacing: 6px;
    font-variant: small-caps;
  }
  .publisher {
    position: absolute;
    bottom: 30px;
    left: 0;
    right: 0;
    display: flex;
    align-items: center;
    justify-content: center;
    gap: 10px;
    font-size: 16px;
    letter-spacing: 2px;
    color: var(--title-white);
  }
  .publisher-dot {
    width: 14px;
    height: 14px;
    border-radius: 50%;
    background: var(--accent-green);
  }
</style>
</head>
<body>
  <main class="canvas">
    <section class="book-cover">
      <h1 class="title">
        <span class="title-line">GAINS BEYOND</span>
        <span class="title-line">THE LANTERN</span>
        <span class="title-accent">GATE</span>
      </h1>
      <p class="subtitle">The only book you need to start investing profitably in Chinese stocks</p>
      <p class="founder-line">FOUNDER OF ORIENTWAGERLY.COM</p>
      <div class="cover-art" role="img" aria-label="Soft glow behind an investing scene of an investor silhouette before stock ticker boards"></div>
      <svg class="market-chart" viewBox="0 0 580 280" aria-label="Rising stock price line chart">
        <line class="grid" x1="0" y1="40" x2="580" y2="40"/>
        <line class="grid" x1="0" y1="110" x2="580" y2="110"/>
        <line class="grid" x1="0" y1="180" x2="580" y2="180"/>
        <line class="grid" x1="0" y1="250" x2="580" y2="250"/>
        <polygon class="trend-area" points="10,240 80,215 140,228 210,180 270,195 330,140 390,158 450,95 510,110 570,40 570,270 10,270"/>
        <polyline class="trend" points="10,240 80,215 140,228 210,180 270,195 330,140 390,158 450,95 510,110 570,40"/>
      </svg>
      <p class="author">Teemu Harkala</p>
      <div class="publisher">
        <span class="publisher-dot"></span>
        <span class="publisher-name">KESTREL LEDGER PRESS</span>
      </div>
    </section>
  </main>
</body>
</html>
```